Project Report for American Indian and Alaska Native org (U.S.)

We need a report formatted/ design / layout.
We are a nonprofit organization that works on indigenous elder issues.
The report should reflect our logo color scheme.
Body font should be at least 11 point sans serif.
Ideally, headings and title would use fonts that are reminiscent of tribal cultures though not hard to read or whimsical/ unprofessional looking.

We have used some light script style fonts in the past -- nothing too cursive looking though.

The audience is public health professionals and tribal staff and leadership.

We want our organization's logo (QR7) and the project logo (brain health) incorporated into the title page.

We prefer the files to come back to us in an editable fashion + a pdf file.

Industry/Entity Type

tribal communities and public health officials

Font styles to use
Serif
Sans Serif

Requirements
Must have
• our logo and color scheme
Should not have
• headdress images

```html
<!DOCTYPE html>
<html lang="en">
<head>
<meta charset="utf-8">
<title>Contents</title>
<link rel="stylesheet" href="https://fonts.googleapis.com/css2?family=Nunito+Sans:wght@700&family=Rye&display=swap">
<style>
  :root {
    --paper: #ffffff;
    --heading-red: #b4564c;
    --ink: #4a4848;
    --rule-teal: #4fa5aa;
  }
  * { margin: 0; padding: 0; box-sizing: border-box; }
  html, body {
    width: 848px;
    height: 1200px;
    overflow: hidden;
    background: var(--paper);
  }
  .page {
    position: relative;
    width: 848px;
    height: 1200px;
    background: var(--paper);
  }
  .contents-title {
    position: absolute;
    left: 38px;
    top: 128px;
    font-family: "Rye", serif;
    font-weight: 400;
    font-size: 31px;
    line-height: 40px;
    letter-spacing: 0.5px;
    color: var(--heading-red);
    text-transform: uppercase;
  }
  .toc {
    position: absolute;
    left: 38px;
    top: 192px;
    width: 710px;
    list-style: none;
    font-family: "Nunito Sans", sans-serif;
    font-weight: 700;
    font-size: 15px;
    line-height: 18px;
    color: var(--ink);
  }
  .toc-entry {
    display: flex;
    justify-content: space-between;
    align-items: flex-start;
    padding: 14px 15px 3px 0;
    border-bottom: 3px solid var(--rule-teal);
  }
  .toc-entry--two-line { padding-bottom: 6px; }
  .toc-label { white-space: pre; }
  .toc-page { min-width: 20px; text-align: right; }
</style>
</head>
<body>
  <main class="page">
    <h1 class="contents-title">Contents</h1>
    <ol class="toc">
      <li class="toc-entry"><span class="toc-label">Executive Summary</span><span class="toc-page">3</span></li>
      <li class="toc-entry"><span class="toc-label">Background</span><span class="toc-page">4</span></li>
      <li class="toc-entry"><span class="toc-label">Road Map for Indian Country</span><span class="toc-page">5</span></li>
      <li class="toc-entry"><span class="toc-label">Tribal Sovereignty</span><span class="toc-page">5</span></li>
      <li class="toc-entry"><span class="toc-label">Process</span><span class="toc-page">6</span></li>
      <li class="toc-entry"><span class="toc-label">Primary Sources</span><span class="toc-page">6</span></li>
      <li class="toc-entry"><span class="toc-label">Secondary Sources</span><span class="toc-page">7</span></li>
      <li class="toc-entry"><span class="toc-label">Road Map Development and Subsequent Activities</span><span class="toc-page">7</span></li>
      <li class="toc-entry"><span class="toc-label">Model Statute Council</span><span class="toc-page">7</span></li>
      <li class="toc-entry toc-entry--two-line"><span class="toc-label">Assembly of State Lawmakers
(Caucus of Native Lawmakers)</span><span class="toc-page">7</span></li>
      <li class="toc-entry"><span class="toc-label">Results</span><span class="toc-page">8</span></li>
      <li class="toc-entry"><span class="toc-label">Related Policy Issues Collections</span><span class="toc-page">8</span></li>
      <li class="toc-entry"><span class="toc-label">State   Alzheimer Plans</span><span class="toc-page">9</span></li>
      <li class="toc-entry"><span class="toc-label">National Plan to Address Alzheimer’s Disease</span><span class="toc-page">11</span></li>
      <li class="toc-entry"><span class="toc-label">Other National Plans</span><span class="toc-page">11</span></li>
      <li class="toc-entry"><span class="toc-label">Conclusion</span><span class="toc-page">11</span></li>
      <li class="toc-entry"><span class="toc-label">Citations</span><span class="toc-page">12</span></li>
    </ol>
  </main>
</body>
</html>
```